Walking Beside the Quiet River; A Study of Refuge, Purpose & Calling

I need a book cover, for the above book title. This is a journey of the heart to know the heart of God. I think on the text, Simple (see below graphic)
Black Lettering for Knowing.....Intimately
Gold lettering for God
Either gold or black for the subtitle; A Study of Refuge, Purpose, & Calling
I would like the below graphic idea only no photograph of a person,
and White background instead of black
Simple Font, like below graphic, but open to suggestions

Target Market(s)

not age specific, Every person has been given a heart to know God, we are taking the mystery out the process to understand God is Father, loving gracious, ever present, etc. If we know His heart, we realize He's not at a distance, He is there, an ever present help

Industry/Entity Type

Security

Requirements
Must have
• Title: Walking Beside the Quiet River; A Study of Refuge, Purpose, & Calling
• My name, Tom Pettigrew
Nice to have
• See Below Graphic

```html
<!DOCTYPE html>
<html lang="en">
<head>
<meta charset="utf-8">
<title>Walking Beside the Quiet River — Tom Pettigrew</title>
<link rel="stylesheet" href="https://fonts.googleapis.com/css2?family=Anton&family=Archivo+Black&family=Oswald:wght@500;700&display=swap">
<style>
  :root {
    --paper: #f4f4f3;
    --paper-shade: #e2e2e0;
    --steel-dark: #0e1418;
    --steel-mid: #3f6470;
    --steel-light: #9fd0da;
    --gold-deep: #5a4618;
    --gold-mid: #b8953e;
    --gold-bright: #f4e08a;
    --gold-pale: #fff6c9;
    --chrome-shadow: #2d2a22;
  }
  html, body {
    margin: 0;
    padding: 0;
    width: 928px;
    height: 1200px;
    overflow: hidden;
    background: var(--paper);
  }
  .cover {
    position: relative;
    width: 928px;
    height: 1200px;
    overflow: hidden;
    background: var(--paper);
  }
  .cover__texture,
  .cover__type {
    position: absolute;
    inset: 0;
    width: 928px;
    height: 1200px;
  }
  .author { font-family: "Oswald", "Arial Narrow", sans-serif; font-weight: 700; letter-spacing: 0; }
  .title-lead { font-family: "Archivo Black", "Arial Black", sans-serif; }
  .title-key { font-family: "Anton", "Impact", sans-serif; }
  .title-tail { font-family: "Anton", "Impact", sans-serif; }
  .subtitle { font-family: "Oswald", "Arial Narrow", sans-serif; font-weight: 700; }
</style>
</head>
<body>
<main class="cover">
  <svg class="cover__texture" viewBox="0 0 928 1200" aria-hidden="true">
    <defs>
      <filter id="stucco" x="0" y="0" width="100%" height="100%">
        <feTurbulence type="fractalNoise" baseFrequency="0.09" numOctaves="3" seed="7" result="noise"/>
        <feDiffuseLighting in="noise" lighting-color="#ffffff" surfaceScale="1.6" result="lit">
          <feDistantLight azimuth="225" elevation="58"/>
        </feDiffuseLighting>
      </filter>
    </defs>
    <rect width="928" height="1200" fill="var(--paper)"/>
    <rect width="928" height="1200" filter="url(#stucco)" opacity="0.55"/>
  </svg>

  <svg class="cover__type" viewBox="0 0 928 1200">
    <defs>
      <linearGradient id="gold-small" x1="0" y1="0" x2="0" y2="1">
        <stop offset="0" stop-color="var(--gold-deep)"/>
        <stop offset="0.35" stop-color="var(--gold-bright)"/>
        <stop offset="0.55" stop-color="var(--gold-pale)"/>
        <stop offset="0.75" stop-color="var(--gold-mid)"/>
        <stop offset="1" stop-color="var(--gold-deep)"/>
      </linearGradient>
      <linearGradient id="steel" x1="0" y1="0" x2="0" y2="1">
        <stop offset="0" stop-color="var(--steel-dark)"/>
        <stop offset="0.38" stop-color="var(--steel-mid)"/>
        <stop offset="0.5" stop-color="var(--steel-light)"/>
        <stop offset="0.62" stop-color="var(--steel-mid)"/>
        <stop offset="1" stop-color="var(--steel-dark)"/>
      </linearGradient>
      <linearGradient id="gold-chrome" x1="0" y1="0" x2="0" y2="1">
        <stop offset="0" stop-color="#ffffff"/>
        <stop offset="0.12" stop-color="#8fa8ae"/>
        <stop offset="0.28" stop-color="var(--gold-bright)"/>
        <stop offset="0.45" stop-color="var(--gold-pale)"/>
        <stop offset="0.58" stop-color="var(--gold-bright)"/>
        <stop offset="0.72" stop-color="var(--gold-mid)"/>
        <stop offset="0.86" stop-color="var(--chrome-shadow)"/>
        <stop offset="1" stop-color="#7a7560"/>
      </linearGradient>
      <filter id="emboss" x="-5%" y="-5%" width="110%" height="115%">
        <feDropShadow dx="2" dy="3" stdDeviation="2" flood-color="#000" flood-opacity="0.35"/>
      </filter>
    </defs>

    <text class="author" x="464" y="178" text-anchor="middle" font-size="64"
          textLength="468" lengthAdjust="spacing"
          fill="url(#gold-small)" stroke="var(--gold-deep)" stroke-width="1" filter="url(#emboss)">TOM PETTIGREW</text>

    <text class="title-lead" x="465" y="478" text-anchor="middle" font-size="96"
          textLength="726" lengthAdjust="spacingAndGlyphs"
          fill="url(#steel)" filter="url(#emboss)">WALKING BESIDE THE</text>

    <text class="title-key" x="456" y="955" text-anchor="middle" font-size="420"
          textLength="768" lengthAdjust="spacingAndGlyphs"
          fill="url(#gold-chrome)" stroke="#8a4b2c" stroke-width="1.5" filter="url(#emboss)">QUIET</text>

    <text class="title-tail" x="457" y="1090" text-anchor="middle" font-size="142"
          textLength="766" lengthAdjust="spacingAndGlyphs"
          fill="url(#steel)" filter="url(#emboss)">RIVER</text>

    <text class="subtitle" x="451" y="1146" text-anchor="middle" font-size="54"
          textLength="754" lengthAdjust="spacingAndGlyphs"
          fill="url(#gold-small)" stroke="var(--gold-deep)" stroke-width="0.8" filter="url(#emboss)">A STUDY OF REFUGE, PURPOSE, &amp; CALLING</text>
  </svg>
</main>
</body>
</html>
```